Meridale Teen Houses QUILT Poster

We need a poster to put up around our Community/Youth Centers that shows the acronym Q.U.I.L.T. which stands for the traits our that make up the culture and personalities of our youth, families and staff. We would like the color scheme to be in our brand colors, and will send them as an upload (grey, blue, green). The poster must have our logo & tagline (uploaded), which may be small and not central. It should have the acronym with the associated words spelled out - as the smaller descriptive words as shown in uploaded attachment. It should be fun - youth friendly (ages 3-18) and really pop. I have also uploaded a sample poster that we created - but don't like....it feels boring, uninspired. It must say "The MTH" Q.U.I.L.T as QUILT is also the name of a different youth agency and we don't want our acronym to be confused with their name. Finally - to tell you a bit more about our organization I have uploaded our annual report. We can't way to see your ideas!!

Target Market(s)

Internal Information Poster for our community centers

Industry/Entity Type

Education

Other font styles liked:
• FUN

Requirements
Must have
• It must say "The MTH" Q.U.I.L.T as QUILT is also the name of a different youth agency and we don't want our acronym to be confused with their name
• The MTH Q.U.I.L.T. - and associated words - should be dominant/prevalent ....
Nice to have
• Fun Images/photos of actual sparks....
Should not have
• As described w/uploads

```html
<!DOCTYPE html>
<html lang="en">
<head>
<meta charset="utf-8">
<title>Meridale Teen Houses – Q.U.I.L.T. Poster</title>
<link rel="stylesheet" href="https://fonts.googleapis.com/css2?family=Black+Ops+One&family=Luckiest+Guy&display=swap">
<style>
  :root {
    --blue-core: #3f86d8;
    --blue-mid: #2a5fb8;
    --blue-edge: #1b3a86;
    --panel-white: #ffffff;
    --panel-grey: #8e8f91;
    --trait-green: #7cc243;
    --trait-white: #ffffff;
    --logo-tint: #a9c6de;
    --letter-red: #e4312b;
    --letter-orange: #f5a11c;
    --letter-yellow: #f6c21b;
    --letter-green: #5fb844;
    --letter-blue: #49a3f0;
    --letter-shade: #12306e;
  }
  html, body {
    margin: 0;
    padding: 0;
    width: 791px;
    height: 1200px;
    overflow: hidden;
    background: var(--blue-edge);
  }
  .poster {
    display: block;
    width: 791px;
    height: 1200px;
  }
  .trait-list {
    font-family: "Black Ops One", "Arial Black", sans-serif;
    font-size: 11.5px;
    letter-spacing: 0.2px;
  }
  .trait-list--green { fill: var(--trait-green); }
  .trait-list--white { fill: var(--trait-white); }
  .panel--white { fill: var(--panel-white); }
  .panel--grey { fill: var(--panel-grey); }

  .acronym { font-family: "Luckiest Guy", "Arial Black", sans-serif; }
  .acronym-prefix { font-size: 14px; fill: var(--trait-white); letter-spacing: 1px; }
  .acronym-letter { font-size: 64px; paint-order: stroke; stroke: var(--letter-shade); stroke-width: 3px; }
  .acronym-word { font-size: 15px; paint-order: stroke; stroke: var(--letter-shade); stroke-width: 1.5px; }
  .tone-red { fill: var(--letter-red); }
  .tone-orange { fill: var(--letter-orange); }
  .tone-yellow { fill: var(--letter-yellow); }
  .tone-green { fill: var(--letter-green); }
  .tone-blue { fill: var(--letter-blue); }

  .brand-name {
    font-family: "Black Ops One", "Arial Black", sans-serif;
    font-size: 9.5px;
    fill: var(--logo-tint);
  }
  .brand-dot { fill: var(--logo-tint); }
</style>
</head>
<body>
<svg class="poster" viewBox="0 0 414 628" width="791" height="1200" xmlns="http://www.w3.org/2000/svg">
  <defs>
    <radialGradient id="backdrop" cx="50%" cy="48%" r="70%">
      <stop offset="0%" stop-color="#3f86d8"/>
      <stop offset="55%" stop-color="#2a5fb8"/>
      <stop offset="100%" stop-color="#1b3a86"/>
    </radialGradient>
  </defs>

  <rect class="backdrop" width="414" height="628" fill="url(#backdrop)"/>

  <!-- corner panels -->
  <polygon class="panel panel--white" points="0,40 160,0 232,0 0,238"/>
  <polygon class="panel panel--grey" points="248,78 336,0 414,0 414,335 388,355"/>
  <polygon class="panel panel--grey" points="0,470 142,482 158,628 0,628"/>
  <polygon class="panel panel--white" points="298,548 414,408 414,560 340,578"/>

  <!-- trait groups -->
  <g class="trait-list trait-list--green" text-anchor="end" transform="translate(105,55) rotate(-38)">
    <text x="0" y="0">PERSISTENT</text>
    <text x="0" y="13">GOAL ORIENTED</text>
    <text x="0" y="26">ENGAGED</text>
    <text x="0" y="39">CREATIVE INNOVATOR</text>
  </g>

  <g class="trait-list trait-list--white" transform="translate(292,48) rotate(57)">
    <text x="0" y="0">WARM AND WELCOMING</text>
    <text x="0" y="14">CONFIDENT COMMUNICATOR</text>
    <text x="0" y="28">POSITIVE ATTITUDE</text>
  </g>

  <g class="trait-list trait-list--white" transform="translate(130,492) rotate(8)">
    <text x="0" y="0" text-anchor="end">ACCOUNTABLE</text>
    <text x="0" y="16" text-anchor="end">COMMITTED</text>
    <text x="0" y="32" text-anchor="end">SELF-REGULATING</text>
  </g>

  <g class="trait-list trait-list--green" transform="translate(314,470) rotate(-53)">
    <text x="0" y="0">EMPATHETIC</text>
    <text x="0" y="14">COLLABORATIVE</text>
    <text x="0" y="28">HELPFUL</text>
  </g>

  <!-- central acronym -->
  <g class="acronym">
    <text class="acronym-prefix" x="108" y="238" transform="rotate(-8 108 238)">THE MTH</text>

    <text class="acronym-letter tone-blue" x="118" y="292">U.</text>
    <text class="acronym-word tone-green" x="156" y="250" transform="rotate(-22 156 250)">nderstanding</text>

    <text class="acronym-letter tone-green" x="204" y="292">I.</text>
    <text class="acronym-word tone-green" x="236" y="268" transform="rotate(-20 236 268)">nclusive</text>

    <text class="acronym-letter tone-red" x="70" y="346">Q.</text>
    <text class="acronym-word tone-red" x="62" y="374" transform="rotate(-10 62 374)">uestioning</text>

    <text class="acronym-letter tone-orange" x="150" y="346">L.</text>
    <text class="acronym-word tone-orange" x="166" y="372">oyal</text>

    <text class="acronym-letter tone-yellow" x="228" y="346">T.</text>
    <text class="acronym-word tone-yellow" x="280" y="336" transform="rotate(-25 280 336)">rustworthy</text>
  </g>

  <g class="trait-list trait-list--white" text-anchor="middle">
    <text x="226" y="416">RESILIENT</text>
    <text x="226" y="431">RESOURCEFUL</text>
    <text x="226" y="446">WILLING</text>
    <text x="226" y="461">CRITICAL THINKER</text>
  </g>

  <!-- brand -->
  <g class="brand">
    <circle class="brand-dot" cx="214" cy="599" r="5"/>
    <text class="brand-name" x="223" y="603">MERIDALE TEEN HOUSES</text>
  </g>
</svg>
</body>
</html>
```